Meadowlark Seedhouse - New Strain Icons, Free seeds & delivery shipping icon and Discreet/Secure shippin

Hi guys - this is quite a big project and requires a full set of icons to be considered for completion. I've extended the project duration to 10 days to allow time for this.
We've just launched our mobile site and we're performing some clean ups of the images ready for a press launch.
Each image is required to be .png 50x50 - this is mandatory.
New Strain Icons - As you can see on each section on the homepage (screenshots provided below), there is an image for a strain. Looks very plain, we want it to have images/logos there that make it obvious that it's either for Bestseller, High Strength etc. - be creative and keep them all in theme with each other.
Free Seeds & Free Delivery - Part of our excellent customer satisfaction promise, we do different deals which offer customers some free seeds with their order. We also offer free shipping on orders at $99 or over! This information doesn't necessarily need to be on the image we just want the idea of free seeds and free delivery to stand out a SINGLE good image.
Underneath the Free Seeds & Free delivery section, there is going to be another section added about half the width of the sections already on there for our USPs of discreet shipping and secure shipping. We want two 50 x 50 images for this - I think maybe a ninja would be cool for the discreet shipping but it's your designs so be creative.
Like I said - it's a lot of work and I want it to be consistent all throughout the designs.

```html
<!DOCTYPE html>
<html lang="en">
<head>
<meta charset="utf-8">
<title>Meadowlark Seedhouse – Mobile Homepage Sections</title>
<link href="https://fonts.googleapis.com/css2?family=Pathway+Gothic+One&family=Inter:wght@400;500&display=swap" rel="stylesheet">
<style>
  :root{
    --stage:#24282c;
    --pink:#b7467f;
    --purple:#5b5993;
    --blue:#4493c9;
    --green:#77c900;
    --green-text:#1f3a00;
    --divider:#dadada;
    --panel-dark:#434343;
    --footer-dark:#2f2f2f;
    --white:#ffffff;
    --tile:#f1f1f1;
    --tile-text:#3a3a3a;
    --footer-green:#7bcc10;
  }
  *{box-sizing:border-box;margin:0;padding:0}
  html,body{width:1200px;height:1200px;overflow:hidden;background:var(--stage)}
  body{position:relative;font-family:"Pathway Gothic One",sans-serif;color:var(--white)}
  h2,h3{font-weight:400}

  .screen{position:absolute;width:480px;overflow:hidden;background:var(--divider)}
  .screen--home{left:100px;top:149px;height:1051px}
  .screen--lower{left:620px;top:0;height:1050px}

  .status-bar{position:absolute;left:0;top:0;width:480px;height:38px;background:#f7f7f7;color:#111;
    font-family:"Inter",sans-serif;font-size:14px;font-weight:500;display:flex;align-items:center;justify-content:space-between;padding:0 8px}
  .status-bar__right{display:flex;align-items:center;gap:6px}
  .battery{width:28px;height:12px;border:1.5px solid #111;border-radius:3px;padding:1px;position:relative}
  .battery::after{content:"";position:absolute;right:-4px;top:3px;width:2px;height:4px;background:#111}
  .battery span{display:block;height:100%;width:89%;background:#111;border-radius:1px}

  .section{position:absolute;left:0;width:480px;overflow:hidden}
  .promo--strength{top:38px;height:245px;background:var(--pink)}
  .promo--autos{top:295px;height:270px;background:var(--purple)}
  .banks--home{top:578px;height:403px;background:var(--blue)}
  .perks--home{top:993px;height:80px;background:var(--panel-dark)}

  .strip-top{top:0;height:18px;background:#3a3b55}
  .banks--lower{top:30px;height:402px;background:var(--blue)}
  .perks--lower{top:444px;height:327px;background:var(--panel-dark)}
  .footer{top:783px;height:267px;background:var(--footer-dark)}

  .promo__title{position:absolute;left:26px;top:36px;font-size:42px;line-height:46px;display:flex;align-items:center;gap:12px}
  .promo__title svg{width:32px;height:32px}
  .promo__text{position:absolute;left:26px;font-size:26px;line-height:31px}
  .promo__btn{position:absolute;left:26px;width:278px;height:63px;border-radius:4px;background:var(--green);
    color:var(--green-text);font-size:29px;display:flex;align-items:center;justify-content:center}
  .promo__art{position:absolute;border-radius:40%}

  .banks__heading{position:absolute;left:0;right:0;top:20px;display:flex;justify-content:center;align-items:center;gap:12px;font-size:45px;line-height:48px}
  .banks__heading svg{width:32px;height:32px}
  .bank{position:absolute;width:126px}
  .bank__tile{height:82px;background:var(--tile);border-radius:2px;display:flex;align-items:center;justify-content:center;
    color:var(--tile-text);font-size:17px;text-align:center;padding:0 8px;line-height:19px}
  .bank__name{margin-top:4px;font-size:22px;line-height:24px;color:#eaf4fb}

  .perk{position:absolute;top:36px;width:212px}
  .perk svg{width:34px;height:34px}
  .perk__title{margin-top:16px;font-size:34px;line-height:37px}
  .perk__text{margin-top:8px;font-size:20px;line-height:24px;color:#e6e6e6}
  .perks__rule{position:absolute;left:240px;top:36px;width:1px;height:168px;background:#777}
  .perks__btn{position:absolute;left:26px;top:235px;width:429px;height:64px;border-radius:4px;background:var(--green);
    color:var(--green-text);font-size:29px;display:flex;align-items:center;justify-content:center}

  .footer__col{position:absolute;top:30px}
  .footer__heading{display:flex;align-items:center;gap:9px;color:var(--footer-green);font-size:30px;line-height:32px;height:32px}
  .footer__heading svg{width:32px;height:32px}
  .footer__links{list-style:none;margin-top:10px}
  .footer__links li{font-size:28px;line-height:42.5px}
</style>
</head>
<body>

<div class="screen screen--home">
  <div class="status-bar">
    <span>●●○○○ Vellacom UK</span>
    <span>10:44</span>
    <span class="status-bar__right">89% <span class="battery"><span></span></span></span>
  </div>

  <section class="section promo--strength">
    <h2 class="promo__title">
      <svg viewBox="0 0 32 32" fill="none" stroke="#fff" stroke-width="2.4" stroke-linejoin="round"><path d="M16 3 L30 29 H2 Z"/><path d="M16 12 l-4 8 h7 l-4 6" stroke-width="2"/></svg>
      High Strength
    </h2>
    <p class="promo__text" style="top:114px">Super High THC Seeds , 15% THC+</p>
    <div class="promo__btn" style="top:151px">Buy High THC seeds</div>
    <div class="promo__art" role="img" aria-label="Purple cannabis bud illustration" style="left:328px;top:41px;width:124px;height:116px;background:radial-gradient(circle at 45% 45%,#b13ec8,#6e1a7e 75%)"></div>
  </section>

  <section class="section promo--autos">
    <h2 class="promo__title">
      <svg viewBox="0 0 32 32" fill="none" stroke="#fff" stroke-width="2.2" stroke-linejoin="round"><path d="M12 4 h8 M14 4 v9 L5 28 h22 L18 13 V4"/><circle cx="14" cy="22" r="1.5" fill="#fff"/><circle cx="19" cy="19" r="1.2" fill="#fff"/></svg>
      Big Yield Autos
    </h2>
    <p class="promo__text" style="top:102px">Well over 1500 + Auto flowering<br>High Yielders</p>
    <div class="promo__btn" style="top:177px">Buy High Yield Autos</div>
    <div class="promo__art" role="img" aria-label="Green cannabis plant illustration" style="left:324px;top:44px;width:128px;height:128px;background:radial-gradient(circle at 50% 50%,#6a9a2a,#2f5510 75%)"></div>
  </section>

  <section class="section banks--home">
    <h2 class="banks__heading">
      <svg viewBox="0 0 32 32" fill="none" stroke="#fff" stroke-width="2.4"><circle cx="16" cy="16" r="14"/><path d="M10 15 h3 v9 h-3z M13 15 l4-6 c1.5 0 2 1 1.5 3 l-0.5 2 h4 c1.2 0 1.8 1 1.5 2 l-1.5 6 c-0.3 1-1 1.5-2 1.5 H13" fill="#fff" stroke="none"/></svg>
      TOP SEED BANKS
    </h2>
    <div class="bank" style="left:26px;top:90px"><div class="bank__tile">Northfield Genetics</div><div class="bank__name">Northfield Genetics</div></div>
    <div class="bank" style="left:177px;top:90px"><div class="bank__tile">Greenwell Seeds</div><div class="bank__name">Greenwell Seeds</div></div>
    <div class="bank" style="left:328px;top:90px"><div class="bank__tile">Harvest Select</div><div class="bank__name">Harvest Select</div></div>
    <div class="bank" style="left:26px;top:251px"><div class="bank__tile">Copperhill Farm</div><div class="bank__name">Copperhill Farm</div></div>
    <div class="bank" style="left:177px;top:251px"><div class="bank__tile">Dr Larkspur</div><div class="bank__name">Dr Larkspur</div></div>
    <div class="bank" style="left:328px;top:251px"><div class="bank__tile">Brisk Bloomery</div><div class="bank__name">Brisk Bloomery</div></div>
  </section>

  <section class="section perks--home">
    <div class="perk" style="left:26px;top:37px">
      <svg viewBox="0 0 34 34" fill="#888"><rect x="1" y="2" width="20" height="14" rx="1"/><path d="M22 7 h6 l5 6 v6 h-11z"/><circle cx="8" cy="22" r="3"/><circle cx="26" cy="22" r="3"/></svg>
    </div>
    <div class="perks__rule" style="top:40px;background:#666"></div>
    <div class="perk" style="left:258px;top:37px">
      <svg viewBox="0 0 34 34" fill="#888"><path d="M4 9 L15 3 L26 9 L15 15Z M4 11 L14 17 V30 L4 24Z M16 17 L26 11 V18 L16 30Z"/></svg>
    </div>
  </section>
</div>

<div class="screen screen--lower">
  <div class="section strip-top"></div>

  <section class="section banks--lower">
    <h2 class="banks__heading">
      <svg viewBox="0 0 32 32" fill="none" stroke="#fff" stroke-width="2.4"><circle cx="16" cy="16" r="14"/><path d="M10 15 h3 v9 h-3z M13 15 l4-6 c1.5 0 2 1 1.5 3 l-0.5 2 h4 c1.2 0 1.8 1 1.5 2 l-1.5 6 c-0.3 1-1 1.5-2 1.5 H13" fill="#fff" stroke="none"/></svg>
      TOP SEED BANKS
    </h2>
    <div class="bank" style="left:26px;top:89px"><div class="bank__tile">Northfield Genetics</div><div class="bank__name">Northfield Genetics</div></div>
    <div class="bank" style="left:177px;top:89px"><div class="bank__tile">Greenwell Seeds</div><div class="bank__name">Greenwell Seeds</div></div>
    <div class="bank" style="left:328px;top:89px"><div class="bank__tile">Harvest Select</div><div class="bank__name">Harvest Select</div></div>
    <div class="bank" style="left:26px;top:251px"><div class="bank__tile">Copperhill Farm</div><div class="bank__name">Copperhill Farm</div></div>
    <div class="bank" style="left:177px;top:251px"><div class="bank__tile">Dr Larkspur</div><div class="bank__name">Dr Larkspur</div></div>
    <div class="bank" style="left:328px;top:251px"><div class="bank__tile">Brisk Bloomery</div><div class="bank__name">Brisk Bloomery</div></div>
  </section>

  <section class="section perks--lower">
    <div class="perk" style="left:25px">
      <svg viewBox="0 0 34 34" fill="#fff"><rect x="1" y="3" width="20" height="13" rx="1"/><text x="3" y="13" font-size="8" font-family="Inter,sans-serif" font-weight="500" fill="#434343">FREE</text><path d="M1 18 h32 v4 H1z M22 8 h6 l5 6 v3 h-11z"/><circle cx="8" cy="25" r="3.5"/><circle cx="26" cy="25" r="3.5"/></svg>
      <h3 class="perk__title">Free Seeds &amp;<br>Delivery</h3>
      <p class="perk__text">Our free seeds are exclusive branded and sought after.</p>
    </div>
    <div class="perks__rule"></div>
    <div class="perk" style="left:258px">
      <svg viewBox="0 0 34 34" fill="#fff"><path d="M3 8 L14 2 L25 8 L14 14Z M3 10 L13 16 V30 L3 24Z M15 16 L25 10 V18 L15 30Z"/><rect x="21" y="23" width="11" height="9" rx="1"/><path d="M23.5 23 v-3 a3 3 0 0 1 6 0 v3" fill="none" stroke="#fff" stroke-width="1.8"/></svg>
      <h3 class="perk__title">Discreet &amp; Secure<br>Shipping</h3>
      <p class="perk__text">We ship your packages totally discreet on all orders.</p>
    </div>
    <div class="perks__btn">View Free Seed Deals</div>
  </section>

  <footer class="section footer">
    <div class="footer__col" style="left:14px">
      <h3 class="footer__heading">
        <svg viewBox="0 0 32 32" fill="none" stroke="var(--footer-green)" stroke-width="2"><path d="M14 4 h14 v12 h-4 l-4 4 v-4 h-6z" fill="var(--footer-green)"/><circle cx="12" cy="20" r="9" fill="var(--footer-dark)"/><path d="M12 17 v7 M12 14 v1"/></svg>
        SUPPORT
      </h3>
      <ul class="footer__links">
        <li>Track your order</li>
        <li>Delivery times</li>
        <li>Shipping information</li>
        <li>Returns</li>
      </ul>
    </div>
    <div class="footer__col" style="left:255px">
      <h3 class="footer__heading">
        <svg viewBox="0 0 32 32" fill="none" stroke="var(--footer-green)" stroke-width="2.4"><circle cx="16" cy="16" r="14"/><path d="M16 14 v10 M16 8 v2"/></svg>
        USEFUL LINKS
      </h3>
      <ul class="footer__links">
        <li>Privacy policy</li>
        <li>Payment methods</li>
        <li>FAQs</li>
        <li>Disclaimer</li>
      </ul>
    </div>
  </footer>
</div>

</body>
</html>
```